Business Card For Life Coaching Business For Men

Take my existing logo and apply it to a business card. I would like the logo to be prominent with stylistic text below reading Life Coaching For Men. Contact info should show as:
Dale Hartwig
dale@steadforgepath.com

```html
<!DOCTYPE html>
<html lang="en">
<head>
<meta charset="utf-8">
<title>Steadforge Path – Business Card</title>
<link rel="stylesheet" href="https://fonts.googleapis.com/css2?family=Oswald:wght@300;400;500&display=swap">
<style>
  :root {
    --navy: #2a2f86;
    --teal: #13837f;
    --teal-glow: #12807f;
    --edge-blue: #283a8a;
    --mist: #9fb3c8;
    --paper: #ffffff;
    --watermark: #eef0f2;
    --ink-soft: #6f7378;
    --backdrop: #e9e6e1;
  }
  * { box-sizing: border-box; margin: 0; padding: 0; }
  html, body {
    width: 1200px; height: 900px; overflow: hidden;
    background: var(--backdrop);
  }
  .canvas {
    position: relative; width: 1200px; height: 900px;
    display: flex; flex-direction: column; align-items: center; justify-content: center; gap: 60px;
  }
  .card {
    position: relative; width: 560px; height: 320px; overflow: hidden;
    box-shadow: 0 6px 18px rgba(0,0,0,0.18);
  }

  /* Shared brand lockup */
  .brand { display: flex; align-items: center; gap: 16px; }
  .brand__dot {
    flex: none; width: 64px; height: 64px; border-radius: 50%;
    border: 6px solid currentColor;
  }
  .brand__text { display: flex; flex-direction: column; }
  .brand__name {
    font-family: "Oswald", sans-serif; font-weight: 500;
    text-transform: uppercase; line-height: 0.95; letter-spacing: 0.5px;
  }
  .brand__tagline {
    margin-top: 8px;
    font-family: "Oswald", sans-serif; font-weight: 400;
    font-size: 13px; line-height: 1; letter-spacing: 3px; text-transform: uppercase;
  }

  /* Front */
  .card--front {
    background: radial-gradient(ellipse at 50% 48%, var(--teal-glow) 0%, #176f84 40%, var(--edge-blue) 100%);
    display: flex; align-items: center; justify-content: center;
  }
  .card--front .brand { color: var(--paper); }
  .card--front .brand__name { font-size: 44px; }

  /* Back */
  .card--back { background: var(--paper); }
  .card__decor {
    position: absolute; left: 350px; top: 14px;
    width: 196px; height: 196px; border-radius: 50%;
    border: 22px solid var(--watermark);
  }
  .card--back .brand {
    position: absolute; left: 40px; top: 116px; color: var(--navy);
  }
  .card--back .brand__dot { width: 70px; height: 70px; }
  .card--back .brand__name { font-size: 44px; }
  .card--back .brand__tagline { color: var(--teal); }
  .contact {
    position: absolute; left: 40px; right: 40px; top: 240px;
    border-top: 1px solid var(--mist); border-bottom: 1px solid var(--mist);
    padding: 8px 0 6px; display: flex; align-items: center; gap: 10px;
    font-family: "Oswald", sans-serif;
  }
  .contact__name {
    font-weight: 500; font-size: 22px; letter-spacing: 0.5px;
    text-transform: uppercase; color: var(--teal);
  }
  .contact__divider { width: 2px; height: 22px; background: var(--navy); }
  .contact__email {
    display: flex; align-items: center; gap: 8px;
    font-weight: 300; font-size: 19px; color: var(--ink-soft);
  }
  .contact__icon { width: 20px; height: 14px; color: var(--teal); }
</style>
</head>
<body>
<main class="canvas">
  <section class="card card--front" aria-label="Card front">
    <div class="brand">
      <span class="brand__dot"></span>
      <div class="brand__text">
        <div class="brand__name">Steadforge<br>Path</div>
        <div class="brand__tagline">Life Coaching For Men</div>
      </div>
    </div>
  </section>

  <section class="card card--back" aria-label="Card back">
    <div class="card__decor" aria-hidden="true"></div>
    <div class="brand">
      <span class="brand__dot"></span>
      <div class="brand__text">
        <div class="brand__name">Steadforge<br>Path</div>
        <div class="brand__tagline">Life Coaching For Men</div>
      </div>
    </div>
    <div class="contact">
      <span class="contact__name">Dale Hartwig</span>
      <span class="contact__divider"></span>
      <span class="contact__email">
        <svg class="contact__icon" viewBox="0 0 20 14" aria-hidden="true">
          <rect x="1" y="1" width="18" height="12" fill="none" stroke="currentColor" stroke-width="2"/>
          <path d="M1 1 L10 8 L19 1" fill="none" stroke="currentColor" stroke-width="2"/>
        </svg>
        dale@steadforgepath.com
      </span>
    </div>
  </section>
</main>
</body>
</html>
```